Paws Forward Academy Business card design

We need a business card for our Dog Training business which is based in the Australian Region of ACT region and surrounds.

We offer a variety of services from group classes in socialisation and obedience training, home visits addressing individual training and behaviour issues.

We also trial and on sell and promote pet products especially specific training and health products for dogs.

We promote responsible pet onwership through supporting adopted dogs through rescue associations and actively assisting and promoting various campaigns hence being the ACT Representative for the National Bluecollar Hound Initiative.
Updates

Looking at current designs that have focussed on making the business's Logo the hero of the branding and marketting.

Delete the: Owner/Trainer

Reason: Still refining current top designs and getting marketting feedback from friends and business managers

Please ensure the 3 lines of details if included is the following;

Professional Dog Training

Dog Behaviour Consultation

Pet Product Sales / Advice

If possible can we add the facebook link in the contact information

facebook.com/PFPupCrew

Target Market(s)

Families and Individuals who are pet dog owners aged 17 to 95 that need support or advice on training and behaviour issues

Industry/Entity Type

Training

Contact Information for Business Card

Paws Forward Academy
Glen Mirrow
Owner / Trainer

Professional Dog Training

0471 863 250
info@pawsforwardacademy.example.au
www.pawsforwardacademy.example.au

Logo styles of interest
Character Logo
Requirements
Must have
• The Paws Forward Academy LOGO incorporated into the card as the Brand representation. Promote and market the logo as the brand.

```html
<!DOCTYPE html>
<html lang="en">
<head>
<meta charset="utf-8">
<title>Paws Forward Academy – Business Card</title>
<link rel="stylesheet" href="https://fonts.googleapis.com/css2?family=Open+Sans:wght@400;600;800&display=swap">
<style>
  :root {
    --bg: #2b2b2b;
    --brand-blue: #2180c6;
    --brand-blue-deep: #1a77b8;
    --ink-grey: #5f5f5f;
    --divider-grey: #6d6d6d;
    --paper: #ffffff;
    --card-w: 900px;
    --card-h: 514px;
  }
  * { box-sizing: border-box; margin: 0; padding: 0; }
  html, body {
    width: 1200px; height: 1200px; overflow: hidden;
    background: var(--bg);
    font-family: "Open Sans", Arial, sans-serif;
  }
  .canvas {
    position: relative; width: 1200px; height: 1200px;
    display: flex; flex-direction: column; align-items: center;
    justify-content: center; gap: 56px;
  }
  .card {
    position: relative; width: var(--card-w); height: var(--card-h);
    box-shadow: 0 10px 30px rgba(0,0,0,.45);
    overflow: hidden;
  }

  /* Front */
  .card-front {
    background: var(--brand-blue);
    display: flex; flex-direction: column; align-items: center; justify-content: center;
    gap: 34px;
  }
  .brand-mark {
    display: flex; align-items: center; gap: 18px;
    font-weight: 800; letter-spacing: .5px; line-height: 1.05;
  }
  .brand-mark .dot {
    width: 34px; height: 34px; border-radius: 50%; flex: none;
  }
  .card-front .brand-mark { color: var(--paper); font-size: 60px; }
  .card-front .brand-mark .dot { background: var(--paper); }
  .front-url {
    color: var(--paper); font-size: 20px; letter-spacing: 3px; font-weight: 400;
  }

  /* Back */
  .card-back { display: flex; background: var(--paper); }
  .back-brand {
    width: 47%; padding: 64px 28px 52px 40px;
    display: flex; flex-direction: column; justify-content: space-between;
  }
  .card-back .brand-mark {
    color: var(--ink-grey); font-size: 42px; gap: 16px; margin-top: 30px;
  }
  .card-back .brand-mark .dot { width: 26px; height: 26px; background: var(--brand-blue); }
  .services { list-style: none; display: flex; flex-direction: column; gap: 12px; }
  .services li {
    display: flex; align-items: center; gap: 12px;
    color: var(--ink-grey); font-weight: 800; font-size: 22px; white-space: nowrap;
  }
  .services li::before {
    content: ""; width: 18px; height: 18px; border-radius: 50%;
    background: var(--brand-blue); flex: none;
  }
  .divider { position: relative; width: 6px; background: var(--divider-grey); }
  .divider svg { position: absolute; left: 4px; top: 46%; }
  .back-contact {
    flex: 1; background: var(--brand-blue-deep); color: var(--paper);
    padding: 56px 36px; display: flex; flex-direction: column; justify-content: center;
  }
  .contact-company { font-weight: 800; font-size: 30px; margin-bottom: 18px; white-space: nowrap; }
  .contact-name { font-weight: 800; font-size: 28px; margin-bottom: 40px; }
  .contact-line { font-weight: 800; font-size: 17px; line-height: 1.8; white-space: nowrap; }
</style>
</head>
<body>
<main class="canvas">
  <section class="card card-front" aria-label="Card front">
    <div class="brand-mark"><span class="dot"></span><span>Paws Forward Academy</span></div>
    <p class="front-url">www.pawsforwardacademy.example.au</p>
  </section>

  <section class="card card-back" aria-label="Card back">
    <div class="back-brand">
      <div class="brand-mark"><span class="dot"></span><span>Paws Forward Academy</span></div>
      <ul class="services">
        <li>Professional Dog Training</li>
        <li>Dog Behaviour Consultation</li>
        <li>Pet Product Sales / Advice</li>
      </ul>
    </div>
    <div class="divider">
      <svg width="12" height="18" viewBox="0 0 12 18" aria-hidden="true"><path d="M0 0 L12 9 L0 18 Z" fill="#6d6d6d"/></svg>
    </div>
    <div class="back-contact">
      <p class="contact-company">Paws Forward Academy</p>
      <p class="contact-name">Glen Mirrow</p>
      <p class="contact-line">0471 863 250</p>
      <p class="contact-line">info@pawsforwardacademy.example.au</p>
      <p class="contact-line">www.pawsforwardacademy.example.au</p>
    </div>
  </section>
</main>
</body>
</html>
```